Investigation Tool App - Static Vornex Ad Image

We need a static image design that promotes our website, which provides an online incident investigation collaboration tool. I would like this static image for Vornex, but I am also seeking the same design in a Taskaro Ad ratio.

We would like to see engaging ad graphics that capture the essence of collaboration, time saving, fast "impact-to-learnings" type vibe. As it helps them collaborate and facilitate the investigation on our interactive canvas and then it has an automated report builder that is AI-assisted to turn their information into coherent sentences in the report, it is not fully AI generated (this is important as i feel people inherently distrust AI generated content).

This tool is aimed at safety professionals in mining, construction and oil & gas who want an easy way to facilitate investigations virtually or in person without having to use whiteboards and double handle information and that want to be able to generate a report and learnings on the same day to quickly prevent further harm.

I have included a bunch of snips of my site and features etc - please feel free to use any of them but dont be constrained by these.

Target Market(s)

Safety Professionals/ Managers in Mining, Oil & Gas & Construction

Industry/Entity Type

Mining, Oil & Gas & Construction

Font styles to use
Sans Serif

Requirements
Nice to have
• Modern, pain point focussed, visual of investigation map and or nodes
Should not have
• No em-dashes, no gimmicky language or terms

```html
<!DOCTYPE html>
<html lang="en">
<head>
<meta charset="UTF-8">
<title>Vornex Ad - Online Incident Investigations</title>
<link rel="stylesheet" href="https://fonts.googleapis.com/css2?family=Montserrat:wght@400;500;800&family=Arimo:wght@400;600;700&display=swap">
<style>
  :root{
    --ink:#121826;
    --white:#ffffff;
    --page:#ffffff;
    --blue:#2b62e6;
    --bezel:#0d0d0f;
    --silver:#c9ccd1;
    --silver-dark:#9a9ea5;
    --ui-bg:#f7f7f8;
    --grid:#e6e7ea;
    --line:#d9dbe0;
    --muted:#7b8190;
    --orange:#f57c22;
    --yellow:#f3c623;
    --node-blue:#2f6fe0;
    --teal:#1a9f8f;
    --navy:#22357a;
    --red:#c8322b;
    --purple:#7b3fc9;
    --green:#2b8a3e;
  }
  *{box-sizing:border-box;margin:0;padding:0}
  html,body{width:1200px;height:1200px;overflow:hidden;background:var(--page)}
  .stage{position:relative;width:1200px;height:1200px;overflow:hidden;background:var(--page)}
  .card-frame{position:absolute;left:70px;top:70px;width:1060px;height:1060px;overflow:hidden;background:var(--white);
    box-shadow:0 0 45px 18px rgba(0,0,0,0.75)}
  .ad{position:absolute;left:0;top:0;width:1200px;height:1200px;transform:scale(0.88333);transform-origin:0 0;background:var(--white);overflow:hidden;font-family:"Montserrat",sans-serif;color:var(--ink)}
  .ad__band{position:absolute;inset:0}
  .headline{position:absolute;top:72px;left:0;width:100%;text-align:center;font-weight:800;font-size:64px;line-height:74px;text-transform:uppercase;letter-spacing:0.5px}
  .subhead{position:absolute;top:222px;left:0;width:100%;text-align:center;font-weight:400;font-size:35px;letter-spacing:0.3px;text-transform:uppercase}
  .lede{position:absolute;top:279px;left:0;width:100%;text-align:center;font-weight:500;font-size:27px;line-height:38px}

  .laptop{position:absolute;left:44px;top:427px;width:1114px;height:640px}
  .laptop__lid{position:absolute;left:104px;top:0;width:907px;height:604px;background:var(--bezel);border-radius:26px 26px 6px 6px;overflow:hidden}
  .laptop__camera{position:absolute;left:50%;top:13px;width:8px;height:8px;margin-left:-4px;border-radius:50%;background:#2a2c31}
  .laptop__base{position:absolute;left:0;top:600px;width:1114px;height:30px;background:linear-gradient(var(--silver),var(--silver-dark));border-radius:2px 2px 40px 40px}
  .laptop__notch{position:absolute;left:50%;top:0;width:150px;height:10px;margin-left:-75px;background:#a7abb2;border-radius:0 0 10px 10px}

  .screen{position:absolute;left:31px;top:37px;width:846px;height:532px;background:var(--ui-bg);overflow:hidden;font-family:"Arimo",sans-serif}
  .sidebar{position:absolute;left:0;top:0;width:50px;height:100%;background:var(--white);border-right:1px solid var(--line)}
  .sidebar__mark{position:absolute;left:12px;top:10px;width:24px;height:24px;background:var(--ink);border-radius:5px}
  .sidebar__toggle{position:absolute;left:13px;top:42px;width:22px;height:22px;border:1px solid var(--line);border-radius:50%}
  .sidebar__icon{position:absolute;left:18px;width:13px;height:12px;background:#555a66;border-radius:2px}
  .sidebar__icon--active{left:13px;width:24px;height:24px;background:#e9ebef;border-radius:6px}
  .sidebar__exit{position:absolute;left:18px;bottom:16px;width:13px;height:13px;border:2px solid #555a66;border-radius:50%}

  .topbar{position:absolute;left:51px;top:0;right:0;height:85px;background:var(--white);border-bottom:1px solid var(--line)}
  .topbar__eyebrow{position:absolute;left:14px;top:22px;font-size:7px;letter-spacing:1px;color:var(--muted);text-transform:uppercase}
  .topbar__title{position:absolute;left:14px;top:36px;font-size:19px;font-weight:700;color:var(--ink)}
  .topbar__desc{position:absolute;left:14px;top:62px;font-size:8px;color:var(--muted)}
  .topbar__account{position:absolute;left:656px;top:28px;font-size:8px;color:var(--muted)}
  .topbar__email{position:absolute;left:708px;top:20px;padding:6px 10px;font-size:9px;font-weight:700;border:1px solid var(--line);border-radius:6px;white-space:nowrap;background:var(--white)}
  .topbar__role{position:absolute;left:746px;top:44px;padding:4px 8px;font-size:8px;font-weight:700;color:var(--navy);background:#e8edfb;border-radius:8px;white-space:nowrap}

  .board{position:absolute;left:51px;top:86px;right:0;bottom:0;background-color:var(--white);
    background-image:linear-gradient(var(--grid) 1px,transparent 1px),linear-gradient(90deg,var(--grid) 1px,transparent 1px);background-size:12px 12px}
  .group{position:absolute;border:1.5px solid #9aa0ab;border-radius:6px;background:rgba(255,255,255,0.55)}
  .group__label{position:absolute;left:6px;top:-6px;font-size:5px;padding:1px 4px;background:var(--white);border:1px solid var(--line);border-radius:3px;color:var(--muted)}
  .tag{position:absolute;width:56px;height:22px;background:var(--orange);color:var(--white);font-size:5px;font-weight:700;padding:4px 5px;clip-path:polygon(0 0,100% 0,100% 80%,50% 100%,0 80%)}
  .hazard{position:absolute;width:68px;height:34px;background:var(--white);border:1px solid var(--ink);border-radius:4px;overflow:hidden;font-size:5px;text-align:center;padding-top:12px;font-weight:700}
  .hazard::before{content:"";position:absolute;left:0;top:0;width:100%;height:8px;background:var(--yellow);border-bottom:1px solid var(--ink)}
  .card{position:absolute;width:58px;height:40px;background:var(--white);border:1px solid var(--line);border-radius:4px;overflow:hidden;font-size:4.5px;text-align:center;padding-top:13px;box-shadow:0 1px 2px rgba(0,0,0,.12)}
  .card__head{position:absolute;left:0;top:0;width:100%;height:8px;color:var(--white);font-size:4px;font-weight:700;padding-top:2px}
  .card__head--blue{background:var(--node-blue)}
  .card__head--red{background:var(--red)}
  .card__head--purple{background:var(--purple)}
  .card__head--green{background:var(--green)}
  .card__score{position:absolute;left:6px;bottom:5px;width:46px;height:4px;background:repeating-linear-gradient(90deg,#56b870 0 6px,transparent 6px 8px)}
  .person{position:absolute;width:34px;height:34px;border-radius:50%;background:#3a3f4a}
  .person__name{position:absolute;width:54px;text-align:center;font-size:4px;color:var(--ink)}
  .system{position:absolute;width:42px;height:42px;border-radius:50%;background:var(--navy);color:var(--white);font-size:4.5px;font-weight:700;text-align:center;padding-top:15px;border:2px solid #9fb3e8}
  .teal-card{position:absolute;width:59px;height:44px;background:var(--white);border:1px solid var(--line);border-radius:3px;font-size:4px;text-align:center;overflow:hidden}
  .teal-card__head{height:8px;background:var(--teal);color:var(--white);padding-top:2px;font-weight:700}

  .brand{position:absolute;left:30px;top:254px;display:flex;align-items:center;gap:8px}
  .brand__square{width:22px;height:22px;background:var(--ink)}
  .brand__name{font-family:"Montserrat",sans-serif;font-weight:800;font-size:20px;color:var(--ink);letter-spacing:0.5px}
  .intro{position:absolute;left:30px;top:305px;width:400px;font-size:13.6px;line-height:19.5px;color:var(--ink)}
</style>
</head>
<body>
<div class="stage">
<div class="card-frame">
<div class="ad">
  <svg class="ad__band" width="1200" height="1200" viewBox="0 0 1200 1200" aria-hidden="true">
    <polygon points="0,970 1200,449 1200,1200 0,1200" fill="var(--blue)"/>
  </svg>

  <h1 class="headline">Still using whiteboards<br>for investigations?</h1>
  <p class="subhead">Move your incident investigations online.</p>
  <p class="lede">Collaborate in real-time, capture insights once, and generate<br>reports instantly.</p>

  <div class="laptop">
    <div class="laptop__lid">
      <span class="laptop__camera"></span>
      <div class="screen">
        <nav class="sidebar">
          <span class="sidebar__mark"></span>
          <span class="sidebar__toggle"></span>
          <span class="sidebar__icon" style="top:82px"></span>
          <span class="sidebar__icon" style="top:112px"></span>
          <span class="sidebar__icon" style="top:142px"></span>
          <span class="sidebar__icon sidebar__icon--active" style="top:166px"></span>
          <span class="sidebar__icon" style="top:202px"></span>
          <span class="sidebar__exit"></span>
        </nav>

        <header class="topbar">
          <span class="topbar__eyebrow">Canvas Creator</span>
          <span class="topbar__title">Canvas Creator</span>
          <span class="topbar__desc">Access every canvas map from one workspace and choose the map category when creating a new one.</span>
          <span class="topbar__account">My account</span>
          <span class="topbar__email">jordan.hale@ridgeline</span>
          <span class="topbar__role">Administrator</span>
        </header>

        <section class="board">
          <div class="group" style="left:28px;top:41px;width:88px;height:157px">
            <span class="group__label">Work Type</span>
            <span class="tag" style="left:15px;top:14px">Working at Heights</span>
            <span class="tag" style="left:15px;top:62px">Working in Hot Works</span>
            <span class="tag" style="left:15px;top:110px">Working Near Water</span>
          </div>

          <div class="group" style="left:146px;top:41px;width:179px;height:157px">
            <span class="group__label">Hazards</span>
            <span class="hazard" style="left:12px;top:12px">Falling Objects</span>
            <span class="hazard" style="left:97px;top:12px">Fall From Heights</span>
            <span class="hazard" style="left:12px;top:60px">Hazardous Fumes</span>
            <span class="hazard" style="left:97px;top:60px">Molten Metal</span>
            <span class="hazard" style="left:12px;top:108px">Water Submersion</span>
            <span class="hazard" style="left:97px;top:108px">Environmental Spill</span>
          </div>

          <span class="tag" style="left:367px;top:81px;width:56px;height:25px">Risk Assessment</span>
          <div class="teal-card" style="left:367px;top:124px">
            <div class="teal-card__head">Key Control</div>
            <div style="padding-top:6px">Site Induction</div>
            <span class="card__score"></span>
          </div>

          <div class="group" style="left:479px;top:41px;width:164px;height:157px">
            <span class="group__label">Controls</span>
            <div class="card" style="left:12px;top:12px"><div class="card__head card__head--blue">Preventative</div>Fall Exclusion Lanyards</div>
            <div class="card" style="left:92px;top:12px"><div class="card__head card__head--blue">Preventative</div>Fall Restraint Anchors</div>
            <div class="card" style="left:12px;top:60px"><div class="card__head card__head--blue">Preventative</div>Positive Pressure Cabinet</div>
            <div class="card" style="left:92px;top:60px"><div class="card__head card__head--blue">Preventative</div>Hot Works PPE</div>
            <div class="card" style="left:12px;top:108px"><div class="card__head card__head--blue">Preventative</div>Guardrails and Restraints</div>
            <div class="card" style="left:92px;top:108px"><div class="card__head card__head--blue">Preventative</div>Bunds and Containment</div>
          </div>

          <div class="group" style="left:674px;top:41px;width:160px;height:72px">
            <span class="group__label">Key Actors</span>
            <span class="person" style="left:10px;top:12px"></span>
            <span class="person__name" style="left:0;top:50px">General Manager</span>
            <span class="person" style="left:58px;top:12px"></span>
            <span class="person__name" style="left:48px;top:50px">Operations Manager</span>
            <span class="person" style="left:106px;top:12px"></span>
          </div>

          <span class="tag" style="left:683px;top:144px;width:54px;height:25px">Site Guidelines</span>

          <div class="group" style="left:479px;top:223px;width:164px;height:222px">
            <span class="group__label">Documents</span>
            <div class="card" style="left:7px;top:12px;width:46px"><div class="card__head card__head--red">System</div>HSE Manual</div>
            <div class="card" style="left:59px;top:12px;width:46px"><div class="card__head card__head--purple">Policy</div>HSE Policy</div>
            <div class="card" style="left:111px;top:12px;width:46px"><div class="card__head card__head--red">Plan</div>HSE Plan</div>
            <div class="card" style="left:7px;top:82px;width:46px"><div class="card__head card__head--red">Procedure</div>Heights Procedure</div>
            <div class="card" style="left:59px;top:82px;width:46px"><div class="card__head card__head--red">Procedure</div>Hot Works Procedure</div>
            <div class="card" style="left:111px;top:82px;width:46px"><div class="card__head card__head--red">Procedure</div>Marine Procedure</div>
            <div class="card" style="left:7px;top:152px;width:46px"><div class="card__head card__head--green">Form</div>Permit to Work</div>
            <div class="card" style="left:59px;top:152px;width:46px"><div class="card__head card__head--green">Form</div>Health Monitoring</div>
            <div class="card" style="left:111px;top:152px;width:46px"><div class="card__head card__head--green">Form</div>Change Control</div>
          </div>

          <div class="group" style="left:674px;top:256px;width:160px;height:72px">
            <span class="group__label">Systems</span>
            <span class="system" style="left:8px;top:12px">Permit to Work</span>
            <span class="system" style="left:60px;top:12px">Safety System</span>
            <span class="system" style="left:112px;top:12px">Change</span>
          </div>

          <div class="brand">
            <span class="brand__square"></span>
            <span class="brand__name">RIDGELINE</span>
          </div>
          <p class="intro">Health &amp; Safety Management Systems are more than just a collection of documents. It is a collection of activities that allow a business to identify and assess information that relates to the safety of a task and their business, so that they can establish guidance materials, systems &amp; processes to ensure work is planned and goes well.</p>
        </section>
      </div>
    </div>
    <div class="laptop__base"><span class="laptop__notch"></span></div>
  </div>
</div>
</div>
</div>
</body>
</html>
```